PWF - world groomers association website

Pacific Whisker Federation (PWF) is a new association located in USA, start the first project in South Korea. As now we do the following business:
1. We supply dog grooming education
2. We certify dog groomers
3. We host dog grooming education events
4. We organize grooming trade show

The design:
Because this organization is related to dog grooming, so beautiful groomed dog images are important. I will upload some well groomed dog images. I want you are able to put all these images or some of the images together either nice color or just layout of the images. I want the first page impressive. This business is related to grooming education, so I want our customers get impressed by visiting our website and decide to contact us for their continuing education. Also since this is an association, I want the website to be some level of institutional. Background layout and images catch eyes, but the content area simple and clear.

I want to be able to edit my site by adding images and edit the contents by myself in a easy way.

I need 5 pages now, but I may need to add more pages, but not more than 8 pages.

www.tollmarden.com is the site I really like.

Thanks.

• consistent tune on every page
• several well-groomed dogs, I can provide images

```html
<!DOCTYPE html>
<html lang="en">
<head>
<meta charset="utf-8">
<title>Pacific Whisker Federation</title>
<link href="https://fonts.googleapis.com/css2?family=Hind:wght@400;500;600;700&family=Open+Sans:wght@400;600;700&display=swap" rel="stylesheet">
<style>
:root{
  --navy:#1b2f5e;
  --navy-soft:#2f4a7a;
  --green:#7dc242;
  --green-dark:#5fa82e;
  --ink:#111;
  --muted:#777;
  --card:#f1f1f1;
  --footer:#1e1e1e;
  --footer-text:#bdbdbd;
  --white:#fff;
}
*{box-sizing:border-box;margin:0;padding:0}
html,body{width:1200px;height:2647px;overflow:hidden}
body{position:relative;background:var(--white);font-family:"Open Sans",sans-serif;color:var(--ink)}
.abs{position:absolute}
.heading{font-family:"Hind",sans-serif}

/* top bar */
.topbar{left:0;top:0;width:1200px;height:42px;background:var(--navy);color:var(--white)}
.topbar .member{left:60px;top:10px;font-size:16px;font-weight:600;display:flex;align-items:center;gap:8px}
.topbar .social{right:60px;top:9px;display:flex;gap:5px}
.topbar .social span{width:24px;height:24px;border-radius:50%;background:var(--white)}

/* header */
.header{left:0;top:42px;width:1200px;height:81px;background:var(--white)}
.info{display:flex;gap:12px;align-items:flex-start}
.info strong{display:block;font-size:17px;font-weight:600}
.info small{font-size:13px;color:#333}
.hours{left:60px;top:22px}
.call{right:60px;top:22px}

/* nav */
.nav{left:0;top:123px;width:1200px;height:43px;background:var(--green)}
.nav a{position:absolute;top:11px;color:var(--white);text-decoration:none;font-size:16px;font-weight:600;font-family:"Hind",sans-serif;letter-spacing:.3px}
.nav a.active:after{content:"";position:absolute;left:0;right:0;bottom:-11px;height:4px;background:var(--navy)}

/* brand */
.brand{left:496px;top:14px;width:208px;height:208px;border-radius:50%;background:var(--white);display:flex;align-items:center;justify-content:center;z-index:3}
.brand .ring{width:184px;height:184px;border-radius:50%;border:4px solid var(--navy);display:flex;align-items:center;justify-content:center}
.brand .name{font-family:"Hind",sans-serif;font-weight:700;font-size:52px;color:var(--navy)}

/* hero */
.hero{left:0;top:166px;width:1200px;height:575px;background:linear-gradient(135deg,#c9c2b6 0%,#e9e6e0 45%,#c3a83f 70%,#8a6a8c 100%)}

/* welcome */
.section-title{left:0;width:1200px;text-align:center;font-family:"Hind",sans-serif;font-weight:700;font-size:37px;color:var(--ink)}
.feature{top:920px;width:369px;height:391px;text-align:center}
.feature.active{background:var(--card)}
.feature .icon{margin:27px auto 0;width:152px;height:152px;border-radius:50%;background:var(--navy);display:flex;align-items:center;justify-content:center}
.feature .icon span{width:138px;height:138px;border-radius:50%;background:var(--green)}
.feature h3{margin-top:28px;font-family:"Hind",sans-serif;font-weight:600;font-size:25px}
.feature p{margin:14px auto 0;width:280px;font-size:12px;line-height:19px;color:var(--muted)}
.btn{display:inline-block;color:var(--white);font-family:"Hind",sans-serif;font-weight:600;font-size:16px;border-radius:2px;text-decoration:none}
.btn.navy{background:var(--navy)}
.btn.green{background:var(--green)}
.feature .btn{margin-top:26px;padding:10px 16px 8px}

/* who we are */
.who-photo{left:0;top:1398px;width:641px;height:378px;background:linear-gradient(120deg,#5c4a36 0%,#d9d2c6 40%,#8c6a50 75%,#3c3028 100%)}
.who{left:641px;top:1398px;width:559px;height:378px;background:var(--navy-soft);color:var(--white);padding:36px 34px 0}
.who h2{font-family:"Hind",sans-serif;font-weight:700;font-size:38px;letter-spacing:.5px}
.who p{margin-top:14px;font-size:13px;line-height:21px}
.who .btn{margin-top:22px;padding:11px 14px 9px;font-size:17px}

/* events */
.arrow{top:2055px}
.event{top:1968px;width:465px;height:233px;background:var(--card);display:flex}
.event .photo{width:219px;height:233px;background:linear-gradient(160deg,#6d5a33 0%,#b69b52 45%,#8a1f24 100%)}
.event .body{padding:9px 12px 0}
.event h4{font-family:"Hind",sans-serif;font-weight:600;font-size:21px}
.event .meta{margin-top:2px;font-size:12px;color:#333;display:flex;gap:14px}
.event p{margin-top:8px;font-size:12px;line-height:19px;color:#444}
.event .btn{margin-top:12px;padding:8px 11px 6px;font-size:15px}

/* footer */
.footer{left:0;top:2286px;width:1200px;height:361px;background:var(--footer);color:var(--footer-text)}
.col-title{top:38px;font-family:"Hind",sans-serif;font-weight:600;font-size:22px;color:#ccc}
.contact-line{display:flex;gap:14px;font-size:14px;line-height:18px;color:#ddd}
.links{top:90px;list-style:none;font-size:14px;line-height:22.5px;color:#ddd}
.links li:before{content:"";display:inline-block;width:5px;height:5px;border-radius:50%;background:var(--green);margin-right:10px;vertical-align:middle}
.field{width:189px;background:#e8e8e8;border-radius:2px;font-size:12px;color:#888;padding:8px 10px}
.foot-social{left:60px;top:222px;display:flex;gap:5px}
.foot-social span{width:24px;height:24px;border-radius:50%;background:#777}
.rule{left:60px;top:2322px;width:1080px;height:1px;background:#3a3a3a}
.copy{left:0;top:332px;width:1200px;text-align:center;font-size:12px;color:#888}
</style>
</head>
<body>

<div class="abs topbar">
  <div class="abs member">
    <svg width="20" height="18" viewBox="0 0 20 18"><path d="M1 2h3l2.5 10h10L19 5H5.5" fill="none" stroke="#fff" stroke-width="2"/><circle cx="8" cy="15.5" r="1.6" fill="#fff"/><circle cx="15" cy="15.5" r="1.6" fill="#fff"/></svg>
    Get Membership
  </div>
  <div class="abs social"><span></span><span></span><span></span><span></span></div>
</div>

<div class="abs header">
  <div class="abs info hours">
    <svg width="24" height="24" viewBox="0 0 24 24"><circle cx="12" cy="12" r="10" fill="none" stroke="#111" stroke-width="2"/><path d="M12 6v6l4 3" fill="none" stroke="#111" stroke-width="2"/></svg>
    <div><strong>Opening Houres</strong><small>Monday to friday | 8:30am to 5:30pm</small></div>
  </div>
  <div class="abs info call">
    <svg width="18" height="24" viewBox="0 0 18 24"><path d="M5 2c-3 1-4 5-2 10s6 9 9 10c2 .5 3-1 4-2l-3-4-2 1c-2-1-4-5-4-7l2-1-1-5z" fill="#111"/></svg>
    <div><strong>Call us on</strong><small>+555014290, 5550188</small></div>
  </div>
</div>

<nav class="abs nav">
  <a class="active" href="#" style="left:58px">HOME</a>
  <a href="#" style="left:145px">ABOUT US</a>
  <a href="#" style="left:264px">MAGAZINES</a>
  <a href="#" style="left:395px">SHOWS</a>
  <a href="#" style="left:719px">VIDEO</a>
  <a href="#" style="left:807px">PRODUCTS</a>
  <a href="#" style="left:931px">VENDORS</a>
  <a href="#" style="left:1047px">CONTACT US</a>
</nav>

<div class="abs brand"><div class="ring"><span class="name">PWF</span></div></div>

<div class="abs hero" role="img" aria-label="Smiling team of groomers in aprons with a small groomed dog in a grooming salon"></div>

<h1 class="abs section-title" style="top:806px">WELCOME TO PACIFIC WHISKER FEDERATION</h1>

<div class="abs feature active" style="left:60px">
  <div class="icon" role="img" aria-label="Icon of a groomer at a table with a dog"><span></span></div>
  <h3>Dog grooming Education</h3>
  <p>Beciegast nveriti vitaesaert asety kertya aserde nerafae kertyuraue styasnemo faseriasera labore et dolore magnam liaseras.</p>
  <a class="btn navy" href="#">Read More</a>
</div>
<div class="abs feature" style="left:440px">
  <div class="icon" role="img" aria-label="Icon of a dog on a rosette award"><span></span></div>
  <h3 style="margin-top:20px">Certify dog Groomers</h3>
  <p>Beciegast nveriti vitaesaert asety kertya aserde nerafae kertyuraue styasnemo faseriasera labore et dolore magnam liaseras.</p>
  <a class="btn green" href="#">Read More</a>
</div>
<div class="abs feature" style="left:802px">
  <div class="icon" role="img" aria-label="Icon of a calendar with a dog"><span></span></div>
  <h3 style="margin-top:20px">Dog grooming Shows</h3>
  <p>Beciegast nveriti vitaesaert asety kertya aserde nerafae kertyuraue styasnemo faseriasera labore et dolore magnam liaseras.</p>
  <a class="btn green" href="#">Read More</a>
</div>

<div class="abs who-photo" role="img" aria-label="Groomer blow-drying a long-haired sheepdog on a grooming table"></div>
<section class="abs who">
  <h2>WHO WE ARE</h2>
  <p>Beciegast nveriti vitaesaert asety kertya aserderafae kertyurauе styasnemo faseriasera labore et dolore magnam liaseras.Beciegast nveriti vitaesaert asety kertya aserderafae kertyuraue styasnemo faseriasera labore et dolore magnam liaseras.Beciegast nveriti vitaesaert asety kertya aserderafae kertyuraue styasnemo faseriasera labore et dolore magnam liaseras.Beciegast nveriti vitaesaert asety kertya aserderafae kertyuraue styasnemo faseriasera labore et dolore magnam liaseras.</p>
  <a class="btn green" href="#">Get Our Membership</a>
</section>

<h2 class="abs section-title" style="top:1864px">DOG GROOMING EVENTS</h2>

<svg class="abs arrow" style="left:60px" width="28" height="50" viewBox="0 0 28 50"><path d="M24 3L4 25l20 22" fill="none" stroke="#2b3545" stroke-width="4"/></svg>
<svg class="abs arrow" style="left:1112px" width="28" height="50" viewBox="0 0 28 50"><path d="M4 3l20 22L4 47" fill="none" stroke="#2b3545" stroke-width="4"/></svg>

<article class="abs event" style="left:125px">
  <div class="photo" role="img" aria-label="Handlers presenting a groomed dog at a show table"></div>
  <div class="body">
    <h4>Beciegast nveriti vitaes</h4>
    <div class="meta"><span>&#9633; 27 May,16</span><span>&#9711; 2:00 pm</span></div>
    <p>Beciegast nveriti vitaesaert asety kertya aserdenerafae kertyuraue styasnemo faseriasera labore et dolore magnam liaseras.Beciegast nveriti vitaesaert asety kertya</p>
    <a class="btn navy" href="#">Read More</a>
  </div>
</article>
<article class="abs event" style="left:609px">
  <div class="photo" role="img" aria-label="Handlers presenting a groomed dog at a show table"></div>
  <div class="body">
    <h4>Beciegast nveriti vitaes</h4>
    <div class="meta"><span>&#9633; 27 May,16</span><span>&#9711; 2:00 pm</span></div>
    <p>Beciegast nveriti vitaesaert asety kertya aserdenerafae kertyuraue styasnemo faseriasera labore et dolore magnam liaseras.Beciegast nveriti vitaesaert asety kertya</p>
    <a class="btn navy" href="#">Read More</a>
  </div>
</article>

<footer class="abs footer">
  <h5 class="abs col-title" style="left:60px">CONTACT US</h5>
  <div class="abs contact-line" style="left:60px;top:106px">
    <svg width="14" height="18" viewBox="0 0 14 18"><path d="M7 0a7 7 0 017 7c0 5-7 11-7 11S0 12 0 7a7 7 0 017-7z" fill="#7dc242"/><circle cx="7" cy="7" r="2.5" fill="#1e1e1e"/></svg>
    <span>48 harbor view lane suite 12<br>portside, ca 90021</span>
  </div>
  <div class="abs contact-line" style="left:60px;top:150px">
    <svg width="16" height="16" viewBox="0 0 18 24"><path d="M5 2c-3 1-4 5-2 10s6 9 9 10c2 .5 3-1 4-2l-3-4-2 1c-2-1-4-5-4-7l2-1-1-5z" fill="#7dc242"/></svg>
    <span># +1800.555.0147</span>
  </div>
  <div class="abs contact-line" style="left:60px;top:180px">
    <svg width="18" height="14" viewBox="0 0 18 14"><rect width="18" height="14" fill="#7dc242"/><path d="M0 0l9 7 9-7" fill="none" stroke="#1e1e1e" stroke-width="1.5"/></svg>
    <span>info@tollmarden.com</span>
  </div>
  <div class="abs foot-social"><span></span><span></span><span></span><span></span></div>

  <h5 class="abs col-title" style="left:404px">OUR SERVICES</h5>
  <ul class="abs links" style="left:407px">
    <li>Home</li><li>Services</li><li>Features</li><li>Support</li><li>About us</li><li>Others</li><li>Contact us</li>
  </ul>

  <h5 class="abs col-title" style="left:660px">QUICK LINKS</h5>
  <ul class="abs links" style="left:660px">
    <li>Home</li><li>Services</li><li>Features</li><li>Support</li><li>About us</li><li>Others</li><li>Contact us</li>
  </ul>

  <h5 class="abs col-title" style="left:951px">ENQUIRY US</h5>
  <div class="abs field" style="left:951px;top:105px;height:36px">Name</div>
  <div class="abs field" style="left:951px;top:149px;height:36px">Email</div>
  <div class="abs field" style="left:951px;top:193px;height:54px">Message</div>
  <a class="abs btn green" href="#" style="left:1057px;top:255px;width:83px;height:34px;text-align:center;padding-top:8px;font-size:17px">Send</a>

  <div class="abs" style="left:60px;top:322px;width:1080px;height:1px;background:#3a3a3a"></div>
  <p class="abs copy">© 2016 &nbsp;PACIFIC WHISKER FEDERATION &nbsp;All Rights Reserved</p>
</footer>

</body>
</html>
```